Landing Page - Mortgage Loan Intake

We are a mortgage company seeking a clean, easy-to-use landing page that consists of minimal copy and creative with a short intake form for customers to sign up to work with us on securing their home financing. We will soon have PX and Google campaigns running throughout the US, and those ads will lead to this landing page. We need at least one landing page for now and may need a slightly different version for A/B testing,. We will expand the project at the beginning of next year with additional versions with the same branding, just geared towards slightly different loan products.

This is the existing intake form we would incorporate on our landing page:

https://apply.quovafin.com/#/create-account

Here is some of the existing content that we would use as a springboard for the design, color scheme, and content of the landing page:

https://brindlehomeloans.com/https://brindlehomeloans.com/about/https://brindlehomeloans.com/refinance/consolidate-debt/

I have also included images that are related to what we're looking for either visually (feel and format) or in terms of the message.

Target Market(s)

people (borrowers) looking for a refinance or debt consolidation through a refinance

Industry/Entity Type

Mortgage Lender

Number of Pages Required

1 page

Font styles to use
Other font styles liked:
• unsure of the name but we would use the font currently used on brindlehomeloans.com

Colors
9bcb3b
cee9f5
ffffff
85acd3
cfeae6
abd036
cadf82
cedeed

Requirements
Must have
• intake form, clean light feel
Nice to have
• explanation of debt consolidation benefits or easy process via a simple infographic or illustration with a clean layout
Should not have
• anything off-brand (colors that are too heavy or not clean and airy)

```html
<!DOCTYPE html>
<html lang="en">
<head>
<meta charset="utf-8">
<title>Brindle Home Loans – Get your loan approved fast</title>
<link href="https://fonts.googleapis.com/css2?family=Open+Sans:wght@400;600;700&display=swap" rel="stylesheet">
<style>
  :root {
    --green: #8dc63f;
    --green-dark: #6fa52a;
    --blue: #85acd3;
    --blue-deep: #6f9bd0;
    --teal: #76a6a3;
    --ink: #3f3f3f;
    --text: #222222;
    --white: #ffffff;
    --footer: #3a3a3a;
    --arrow-bg: #2b2b2b;
  }
  * { box-sizing: border-box; margin: 0; padding: 0; }
  html, body { width: 1102px; height: 1200px; overflow: hidden; background: var(--white); }
  body { font-family: "Open Sans", Arial, sans-serif; color: var(--text); }
  .page { position: relative; width: 1102px; height: 1200px; }

  /* Hero */
  .hero { position: absolute; left: 0; top: 0; width: 1102px; height: 565px; overflow: hidden; }
  .hero-photo {
    position: absolute; inset: 0;
    background: linear-gradient(90deg, #b59a7a 0%, #d9d4cc 14%, #f1f0ee 22%, #f7f7f6 50%, #f3f4f2 75%, #e4e6e2 100%);
  }
  .hero-photo::after {
    content: ""; position: absolute; left: 0; right: 0; bottom: 0; height: 160px;
    background: linear-gradient(180deg, rgba(255,255,255,0) 0%, rgba(200,200,200,.45) 100%);
  }
  .brand { position: absolute; display: flex; align-items: center; gap: 7px; font-weight: 700; color: var(--ink); font-size: 20px; letter-spacing: -0.2px; transform: translateX(-50%); white-space: nowrap; }
  .brand-mark { width: 12px; height: 12px; border-radius: 50%; background: var(--green); }
  .hero .brand { left: 551px; top: 28px; }
  .headline { position: absolute; top: 104px; left: 0; width: 100%; text-align: center; font-size: 40px; font-weight: 600; color: var(--ink); letter-spacing: -0.3px; }

  .slider-arrow { position: absolute; top: 303px; width: 22px; height: 29px; background: var(--arrow-bg); opacity: .85; }
  .slider-arrow svg { display: block; }
  .slider-arrow.prev { left: 0; }
  .slider-arrow.next { right: 0; }

  /* Intake panel */
  .intake { position: absolute; left: 336px; top: 178px; width: 430px; height: 338px; background: rgba(133,172,211,.92); color: var(--white); }
  .intake-title { position: absolute; left: 19px; top: 16px; font-size: 16px; font-weight: 700; white-space: nowrap; }
  .field { position: absolute; left: 19px; width: 180px; height: 34px; background: var(--white); padding: 0 14px; font: 400 10.5px "Open Sans", Arial, sans-serif; color: #555; display: flex; align-items: center; }
  .field.email { top: 57px; }
  .field.confirm { top: 118px; }
  .field.password { top: 179px; }

  .feature { position: absolute; left: 222px; width: 200px; }
  .feature svg { position: absolute; left: 0; top: 2px; }
  .feature h3 { margin-left: 33px; font-size: 15px; font-weight: 400; line-height: 18px; }
  .feature p { margin-left: 33px; font-size: 8.6px; line-height: 13.5px; margin-top: 2px; }
  .feature.secure { top: 54px; }
  .feature.autosave { top: 116px; }
  .feature.paperwork { top: 168px; }

  .create-account { position: absolute; left: 19px; top: 238px; width: 392px; height: 48px; background: var(--green); border: 2px solid var(--green-dark); color: var(--white); font: 700 16.5px "Open Sans", Arial, sans-serif; display: flex; align-items: center; justify-content: center; letter-spacing: .2px; }
  .sign-in-line { position: absolute; left: 0; top: 299px; width: 100%; text-align: center; font-size: 14.5px; font-weight: 600; }
  .sign-in-line span { text-decoration: underline; }

  /* Process */
  .process-title { position: absolute; top: 620px; width: 100%; text-align: center; font-size: 30px; font-weight: 600; color: var(--green); }
  .process-graphic { position: absolute; left: 0; top: 0; }
  .step-label { position: absolute; font-size: 12px; line-height: 17.5px; color: var(--text); }
  .step-label.right-aligned { text-align: right; }
  .step-label.centered { text-align: center; }
  .step-label.goal { color: var(--green); font-size: 14px; }
  .process .brand { left: 551px; top: 1012px; }

  /* Footer */
  .footer { position: absolute; left: 0; top: 1130px; width: 1102px; height: 70px; background: var(--footer); color: var(--white); }
  .copyright { position: absolute; left: 122px; top: 25px; font-size: 11.5px; }
  .social { position: absolute; top: 20px; width: 28px; height: 28px; border-radius: 50%; border: 2px solid #555; }
  .social.one { left: 914px; background: #2f4f8f; }
  .social.two { left: 952px; background: #e03a2f; }
</style>
</head>
<body>
<div class="page">

  <section class="hero">
    <div class="hero-photo" role="img" aria-label="Bright white living room with bookshelves, a yellow lounge chair, a white sofa and a striped rug"></div>
    <div class="brand"><span class="brand-mark"></span>Brindle Home Loans</div>
    <h1 class="headline">Get your loan approved fast.</h1>

    <div class="slider-arrow prev"><svg width="22" height="29" viewBox="0 0 22 29"><path d="M14 7 L8 14.5 L14 22" fill="none" stroke="#fff" stroke-width="1.5"/></svg></div>
    <div class="slider-arrow next"><svg width="22" height="29" viewBox="0 0 22 29"><path d="M8 7 L14 14.5 L8 22" fill="none" stroke="#fff" stroke-width="1.5"/></svg></div>

    <form class="intake">
      <h2 class="intake-title">LET'S GET STARTED ON YOUR LOAN APPLICATION</h2>
      <div class="field email">Email Address</div>
      <div class="field confirm">Confirm email Address</div>
      <div class="field password">Password</div>

      <div class="feature secure">
        <svg width="22" height="26" viewBox="0 0 22 26"><path d="M5 11 V7 a6 6 0 0 1 12 0 V11" fill="none" stroke="#fff" stroke-width="2.6"/><rect x="2" y="11" width="18" height="13" rx="1.5" fill="#fff"/></svg>
        <h3>Secure</h3>
        <p>Your data is protected with industry-standard encryption.</p>
      </div>
      <div class="feature autosave">
        <svg width="24" height="24" viewBox="0 0 24 24"><path d="M2 3 a1 1 0 0 1 1-1 H18 L22 6 V21 a1 1 0 0 1-1 1 H3 a1 1 0 0 1-1-1 Z" fill="#fff"/><rect x="5" y="4" width="12" height="6" fill="#85acd3"/><circle cx="12" cy="16" r="2.6" fill="#85acd3"/></svg>
        <h3>Autosaved</h3>
        <p>We'll save your information as you go.</p>
      </div>
      <div class="feature paperwork">
        <svg width="28" height="22" viewBox="0 0 28 22"><rect x="5" y="3" width="18" height="12" fill="none" stroke="#fff" stroke-width="2"/><path d="M1 17 H27 L25 19 H3 Z" fill="#fff"/></svg>
        <h3>Less paperwork</h3>
        <p>Import income and asset information directly to your application.</p>
      </div>

      <div class="create-account">CREATE ACCOUNT</div>
      <p class="sign-in-line">Already have an account? <span>Sign In</span></p>
    </form>
  </section>

  <section class="process">
    <h2 class="process-title">Brindle Home Loans' Easy Process</h2>

    <svg class="process-graphic" width="1102" height="1130" viewBox="0 0 1102 1130">
      <defs>
        <linearGradient id="arcGradient" x1="334" y1="0" x2="768" y2="0" gradientUnits="userSpaceOnUse">
          <stop offset="0" stop-color="#6f9bd0"/>
          <stop offset="0.5" stop-color="#85b96a"/>
          <stop offset="1" stop-color="#8dc63f"/>
        </linearGradient>
        <g id="gearTeeth">
          <rect x="-2.2" y="-1" width="4.4" height="2" transform="rotate(0)"/>
        </g>
      </defs>
      <path d="M338 1076 A217 217 0 1 1 764 1076" fill="none" stroke="url(#arcGradient)" stroke-width="2.2"/>

      <!-- step circles -->
      <circle cx="280" cy="972" r="52" fill="#6f9bd0"/>
      <circle cx="385" cy="839" r="52" fill="#6f9bd0"/>
      <circle cx="551" cy="787" r="52" fill="#6f9bd0"/>
      <circle cx="717" cy="839" r="52" fill="#6f9bd0"/>
      <circle cx="822" cy="972" r="52" fill="#8dc63f"/>

      <!-- phone -->
      <path d="M268 950 c-6 3 -6 12 -1 20 c5 9 13 17 21 21 c6 3 12 2 14-3 l-8-8 l-6 4 c-4-2-9-8-11-12 l4-6 z" fill="#fff"/>
      <!-- list -->
      <g fill="#fff">
        <rect x="363" y="822" width="11" height="9" rx="1"/><rect x="378" y="822" width="29" height="9" rx="1"/>
        <rect x="363" y="835" width="11" height="9" rx="1"/><rect x="378" y="835" width="29" height="9" rx="1"/>
        <rect x="363" y="848" width="11" height="9" rx="1"/><rect x="378" y="848" width="29" height="9" rx="1"/>
      </g>
      <!-- document search -->
      <path d="M533 766 H556 L570 780 V810 H533 Z" fill="#fff"/>
      <path d="M556 766 V780 H570" fill="none" stroke="#6f9bd0" stroke-width="2"/>
      <circle cx="549" cy="792" r="6" fill="none" stroke="#6f9bd0" stroke-width="2.4"/>
      <path d="M553 797 L559 803" stroke="#6f9bd0" stroke-width="2.8"/>
      <!-- gears -->
      <g fill="#fff">
        <g transform="translate(705 842)">
          <circle r="12"/>
          <rect x="-3.5" y="-17" width="7" height="34" rx="1"/>
          <rect x="-3.5" y="-17" width="7" height="34" rx="1" transform="rotate(45)"/>
          <rect x="-3.5" y="-17" width="7" height="34" rx="1" transform="rotate(90)"/>
          <rect x="-3.5" y="-17" width="7" height="34" rx="1" transform="rotate(135)"/>
          <circle r="5" fill="#6f9bd0"/>
        </g>
        <g transform="translate(734 828)">
          <circle r="6"/>
          <rect x="-2" y="-9" width="4" height="18" rx=".8"/>
          <rect x="-2" y="-9" width="4" height="18" rx=".8" transform="rotate(60)"/>
          <rect x="-2" y="-9" width="4" height="18" rx=".8" transform="rotate(120)"/>
          <circle r="2.4" fill="#6f9bd0"/>
        </g>
        <g transform="translate(734 856)">
          <circle r="6"/>
          <rect x="-2" y="-9" width="4" height="18" rx=".8"/>
          <rect x="-2" y="-9" width="4" height="18" rx=".8" transform="rotate(60)"/>
          <rect x="-2" y="-9" width="4" height="18" rx=".8" transform="rotate(120)"/>
          <circle r="2.4" fill="#6f9bd0"/>
        </g>
      </g>
      <!-- tick -->
      <circle cx="822" cy="972" r="19" fill="#fff"/>
      <path d="M812 972 L819 979 L832 965" fill="none" stroke="#8dc63f" stroke-width="5" stroke-linecap="round" stroke-linejoin="round"/>

      <!-- numbered nodes on the arc -->
      <g font-family="Open Sans, Arial, sans-serif" font-size="13" font-weight="700" fill="#fff" text-anchor="middle">
        <circle cx="346" cy="1008" r="17" fill="#6f9bd0"/><text x="346" y="1013">1</text>
        <circle cx="430" cy="900" r="17" fill="#76a6a3"/><text x="430" y="905">2</text>
        <circle cx="551" cy="862" r="17" fill="#85b96a"/><text x="551" y="867">3</text>
        <circle cx="673" cy="900" r="17" fill="#8dc63f"/><text x="673" y="905">4</text>
        <circle cx="750" cy="1008" r="17" fill="#8dc63f"/><text x="750" y="1013">5</text>
      </g>
    </svg>

    <p class="step-label right-aligned" style="left:104px; top:954px; width:120px;">Contact one of our<br>Mortgage specialists</p>
    <p class="step-label right-aligned" style="left:180px; top:821px; width:140px;">Determine the best<br>loan program for you</p>
    <p class="step-label centered" style="left:481px; top:692px; width:140px;">Our team reviews<br>your documents</p>
    <p class="step-label" style="left:781px; top:821px; width:160px;">We walk you through<br>appraisal and processing</p>
    <p class="step-label goal" style="left:885px; top:962px; width:120px;">Debt Freedom</p>

    <div class="brand"><span class="brand-mark"></span>Brindle Home Loans</div>
  </section>

  <footer class="footer">
    <p class="copyright">Copyright &nbsp;©&nbsp; 2018 &nbsp;Brindle Home Loans. &nbsp; All rights reserved.</p>
    <span class="social one" aria-label="Social profile"></span>
    <span class="social two" aria-label="Social profile"></span>
  </footer>

</div>
</body>
</html>
```